exclusive Speakeasy Bar Web design in New Jersey USA

We are opening a speakeasy in New Jersey USA soon. we are looking for a web designer to do our web site including the coding. we a looking for a 4 to 5 page web design. the site will be mostly static. home page, contact page, menu page and a link to a 3rd party site (most likely Qelmo) for reservations. we are looking for this designer to do our menu deign as well. we are looking for a quick turnaround 7-10 days. i am attaching some pictures for the designers to see the concept design and the actual current pictures with our logo as well. professionally taken pictures will be provided later on. our photographer will be taking the pictures in the next week.

Industry/Entity Type

Restaurant, Bar, Speakeasy

Coding

Coded - Design and coding required

Number of Pages Required

4 page

Requirements
Must have
• home page, contact page, menu page and a link to qelmo.com for reservations
Nice to have
• some videos

```html
<!DOCTYPE html>
<html lang="en">
<head>
<meta charset="utf-8">
<title>Hollis Room — Speakeasy</title>
<link rel="stylesheet" href="https://fonts.googleapis.com/css2?family=Cinzel:wght@400;600&family=Montserrat:wght@400;500;600&display=swap">
<style>
:root{
  --ink:#1e1e1e;
  --slate:#313632;
  --slate-mid:#2d302c;
  --slate-deep:#252624;
  --bronze:#946a2b;
  --gold:#d0a65b;
  --line:rgba(208,166,91,.28);
  --rule:rgba(255,255,255,.09);
  --text:#e9e6df;
  --muted:#bdb8ad;
  --page:#dcdcdc;
}
*{box-sizing:border-box;margin:0;padding:0}
html,body{width:1200px;height:2243px;overflow:hidden;background:var(--page)}
h1,h2,h3{font-weight:400}
.site{position:absolute;left:126px;top:0;width:947px;height:2243px;background:var(--slate);font-family:"Montserrat",sans-serif;color:var(--text);overflow:hidden}
.abs{position:absolute}

/* header frame */
.rail{position:absolute;top:0;width:1px;height:645px;background:var(--rule)}
.rail.left{left:65px}.rail.right{left:882px}
.nav-rule{position:absolute;left:0;top:73px;width:947px;height:1px;background:var(--rule)}
.brand-mark{position:absolute;left:8px;top:16px;width:49px;height:40px;display:flex;align-items:center;justify-content:center;font-family:"Cinzel",serif;font-size:11px;color:var(--gold);letter-spacing:.5px}
.nav{position:absolute;top:28px;left:273px;display:flex;font-family:"Cinzel",serif;font-size:12px;color:var(--text)}
.nav a{color:inherit;text-decoration:none}
.nav .sep{margin:0 28px;color:var(--muted)}
.burger{position:absolute;left:906px;top:30px;width:16px}
.follow{position:absolute;left:26px;top:360px;transform:rotate(-90deg);transform-origin:left top;font-size:9px;color:var(--text);display:flex;align-items:center;gap:8px;white-space:nowrap}
.follow .dot{width:7px;height:7px;border-radius:50%;background:var(--text)}
.book{position:absolute;left:905px;top:363px;transform:rotate(-90deg);transform-origin:left top;font-size:8px;letter-spacing:.5px;color:var(--text);white-space:nowrap}
.book-line{position:absolute;left:921px;top:272px;width:1px;height:92px;background:var(--gold)}

.photo{position:absolute}
.hero{left:65px;top:73px;width:817px;height:381px;background:linear-gradient(180deg,#272c27 0%,#3a3b30 35%,#8a5d2c 62%,#c3843c 78%,#6a4a30 100%)}

.intro-kicker{left:123px;top:512px;font-size:9px;color:var(--gold)}
.intro-title{left:123px;top:527px;font-family:"Cinzel",serif;font-weight:600;font-size:33px;line-height:32px;color:#fff}
.intro-photo{left:433px;top:513px;width:205px;height:76px;background:linear-gradient(90deg,#5a3b23,#a0632f 30%,#7b4d2a 60%,#b07840 80%,#4d3422)}
.btn{position:absolute;border:1px solid var(--bronze);color:var(--text);font-size:9px;display:flex;align-items:center;justify-content:center;letter-spacing:.3px}
.btn.menu{left:716px;top:532px;width:103px;height:36px}

.band{position:absolute;left:0;width:947px;border-top:1px solid var(--rule);border-bottom:1px solid var(--rule);display:flex;align-items:center;justify-content:center;gap:6px;font-family:"Cinzel",serif;font-weight:400;font-size:19px;letter-spacing:.5px;color:#fff}
.band.specials{top:645px;height:56px;background:var(--slate)}
.menu-area{position:absolute;left:0;top:701px;width:947px;height:520px;background:var(--slate-mid)}

.dishes{position:absolute;top:56px;left:126px;display:grid;grid-template-columns:333px 320px;column-gap:42px;row-gap:14px}
.dish{display:flex;align-items:center;height:42px;gap:11px}
.dish-photo{width:42px;height:42px;flex:none;background:radial-gradient(circle at 50% 45%,#d9c9a0 0%,#a4452e 35%,#2a2220 70%)}
.dish.egg .dish-photo{background:radial-gradient(circle at 50% 50%,#e6cf62 0%,#8fa34a 35%,#1f201c 75%)}
.dish-body{flex:1}
.dish-head{display:flex;align-items:center;gap:8px;font-family:"Cinzel",serif;font-size:12px;color:var(--gold)}
.dish-head .leader{flex:1;height:3px;border-top:1px solid var(--line);border-bottom:1px solid var(--line)}
.dish-desc{font-size:8px;color:var(--text);margin-top:4px}
.full-menu{left:442px;top:447px;font-size:8px;font-weight:600;color:#fff;padding-bottom:5px;border-bottom:1px solid var(--gold)}

.video{left:0;top:1221px;width:947px;height:360px;background:radial-gradient(ellipse at 50% 75%,#6b2a1c 0%,#2a1f17 35%,#1a1714 70%),#1a1714}
.play{position:absolute;left:756px;top:1365px}

.band.contact{top:1581px;height:55px;background:var(--slate-deep)}
.contact-area{position:absolute;left:0;top:1636px;width:947px;height:398px;background:var(--slate-deep)}
.contact-photo{left:125px;top:1636px;width:356px;height:398px;background:linear-gradient(180deg,#3a2c22 0%,#8e6234 30%,#5b3a24 55%,#a06c38 75%,#33251c 100%)}
.touch-title{left:540px;top:1750px;font-family:"Cinzel",serif;font-weight:600;font-size:25px;color:#fff}
.touch-copy{left:541px;top:1800px;width:282px;font-size:9.5px;line-height:19px;color:var(--muted)}
.btn.contact{left:540px;top:1878px;width:103px;height:35px}

.footer{position:absolute;left:0;top:2034px;width:947px;height:209px;background:var(--ink);border-top:1px solid var(--rule)}
.foot-brand{left:464px;top:62px;width:43px;height:52px;display:flex;align-items:center;justify-content:center;font-family:"Cinzel",serif;font-size:10px;color:var(--gold);text-align:center;line-height:12px}
.copy{left:464px;top:127px;font-size:7.5px;color:var(--text)}
.foot-h{font-family:"Cinzel",serif;font-size:12px;color:#fff}
.foot-col{top:62px;font-size:7.5px;color:var(--gold);line-height:15px}
.foot-col .foot-h{margin-bottom:8px}
.hours{display:grid;grid-template-columns:64px auto}
</style>
</head>
<body>
<div class="site">

  <header>
    <div class="brand-mark">HOLLIS</div>
    <nav class="nav">
      <a href="#">Home</a><span class="sep">/</span>
      <a href="#">Menu</a><span class="sep">/</span>
      <a href="#">Reservations</a><span class="sep">/</span>
      <a href="#">Contact Us</a>
    </nav>
    <svg class="burger" viewBox="0 0 16 12" width="16" height="12"><path d="M0 1h16M0 6h16M0 11h16" stroke="#d0a65b" stroke-width="1"/></svg>
    <div class="nav-rule"></div>
    <div class="rail left"></div>
    <div class="rail right"></div>
    <div class="follow">Follow Us: <span class="dot"></span><span class="dot"></span></div>
    <div class="book">BOOK YOUR TABLE</div>
    <div class="book-line"></div>
  </header>

  <div class="photo hero" role="img" aria-label="Lounge with tufted leather sofa, amber armchairs and a painted heron mural"></div>

  <section>
    <p class="abs intro-kicker">Discover the Hidden Charm of Our Speakeasy:</p>
    <h1 class="abs intro-title">Where Time<br>Stands Still</h1>
    <div class="photo intro-photo" role="img" aria-label="Backlit bar shelves stocked with spirits"></div>
    <a class="btn menu">OUR MENU</a>
  </section>

  <h2 class="band specials">RECOMMENDED SPECIALITIES<svg width="12" height="12" viewBox="0 0 12 12"><path d="M10 2L2 10M2 4v6h6" stroke="#fff" fill="none" stroke-width="1.2"/></svg></h2>

  <section class="menu-area">
    <div class="dishes">
      <div class="dish"><div class="dish-photo" role="img" aria-label="Lobster canape"></div><div class="dish-body"><div class="dish-head">Lobster Canapes<span class="leader"></span>$10</div><p class="dish-desc">Flavored Cream Cheese or Mayonnaise, Minced Onions, Herbs</p></div></div>
      <div class="dish egg"><div class="dish-photo" role="img" aria-label="Devilled eggs"></div><div class="dish-body"><div class="dish-head">Devilled Eggs<span class="leader"></span>$10</div><p class="dish-desc">Ham, Herbs, Avocado and Sour Cream</p></div></div>
      <div class="dish"><div class="dish-photo" role="img" aria-label="Lobster canape"></div><div class="dish-body"><div class="dish-head">Lobster Canapes<span class="leader"></span>$10</div><p class="dish-desc">Flavored Cream Cheese or Mayonnaise, Minced Onions, Herbs</p></div></div>
      <div class="dish egg"><div class="dish-photo" role="img" aria-label="Devilled eggs"></div><div class="dish-body"><div class="dish-head">Devilled Eggs<span class="leader"></span>$10</div><p class="dish-desc">Ham, Herbs, Avocado and Sour Cream</p></div></div>
      <div class="dish"><div class="dish-photo" role="img" aria-label="Lobster canape"></div><div class="dish-body"><div class="dish-head">Lobster Canapes<span class="leader"></span>$10</div><p class="dish-desc">Flavored Cream Cheese or Mayonnaise, Minced Onions, Herbs</p></div></div>
      <div class="dish egg"><div class="dish-photo" role="img" aria-label="Devilled eggs"></div><div class="dish-body"><div class="dish-head">Devilled Eggs<span class="leader"></span>$10</div><p class="dish-desc">Ham, Herbs, Avocado and Sour Cream</p></div></div>
      <div class="dish"><div class="dish-photo" role="img" aria-label="Lobster canape"></div><div class="dish-body"><div class="dish-head">Lobster Canapes<span class="leader"></span>$10</div><p class="dish-desc">Flavored Cream Cheese or Mayonnaise, Minced Onions, Herbs</p></div></div>
      <div class="dish egg"><div class="dish-photo" role="img" aria-label="Devilled eggs"></div><div class="dish-body"><div class="dish-head">Devilled Eggs<span class="leader"></span>$10</div><p class="dish-desc">Ham, Herbs, Avocado and Sour Cream</p></div></div>
      <div class="dish"><div class="dish-photo" role="img" aria-label="Lobster canape"></div><div class="dish-body"><div class="dish-head">Lobster Canapes<span class="leader"></span>$10</div><p class="dish-desc">Flavored Cream Cheese or Mayonnaise, Minced Onions, Herbs</p></div></div>
      <div class="dish egg"><div class="dish-photo" role="img" aria-label="Devilled eggs"></div><div class="dish-body"><div class="dish-head">Devilled Eggs<span class="leader"></span>$10</div><p class="dish-desc">Ham, Herbs, Avocado and Sour Cream</p></div></div>
      <div class="dish"><div class="dish-photo" role="img" aria-label="Lobster canape"></div><div class="dish-body"><div class="dish-head">Lobster Canapes<span class="leader"></span>$10</div><p class="dish-desc">Flavored Cream Cheese or Mayonnaise, Minced Onions, Herbs</p></div></div>
      <div class="dish egg"><div class="dish-photo" role="img" aria-label="Devilled eggs"></div><div class="dish-body"><div class="dish-head">Devilled Eggs<span class="leader"></span>$10</div><p class="dish-desc">Ham, Herbs, Avocado and Sour Cream</p></div></div>
    </div>
    <a class="abs full-menu">VIEW FULL MENU HERE</a>
  </section>

  <div class="photo video" role="img" aria-label="Bartender stirring a cocktail over ice at the bar"></div>
  <svg class="play" width="68" height="68" viewBox="0 0 68 68">
    <defs><linearGradient id="playFill" x1="0" y1="0" x2="1" y2="1"><stop offset="0" stop-color="#d0a65b"/><stop offset="1" stop-color="#946a2b"/></linearGradient></defs>
    <circle cx="34" cy="34" r="32" fill="url(#playFill)" stroke="#fff" stroke-width="2"/>
    <path d="M28 25v18l15-9z" fill="#fff"/>
  </svg>

  <h2 class="band contact">CONTACT US</h2>
  <section class="contact-area"></section>
  <div class="photo contact-photo" role="img" aria-label="Arched wooden cabinet filled with bottles of spirits"></div>
  <h3 class="abs touch-title">Get In Touch</h3>
  <p class="abs touch-copy">We would love to welcome you to our restaurant and offer you a memorable dining experience! To make a reservation, please do not hesitate to contact us.</p>
  <a class="btn contact">CONTACT US</a>

  <footer class="footer">
    <div class="abs foot-brand">HOLLIS<br>ROOM</div>
    <p class="abs copy">© 2023</p>
    <div class="abs foot-col" style="left:560px">
      <div class="foot-h">LET'S CONECT</div>
      info@hollisroom.com<br>+1 555 014 2290<br>48 Riverside Avenue,<br>Harbor City
    </div>
    <div class="abs foot-col" style="left:706px">
      <div class="foot-h">OPENING HOURS</div>
      <div class="hours"><span>Tue to Sun</span><span>16:00-01:00</span><span>Mon</span><span>Closed</span></div>
    </div>
  </footer>

</div>
</body>
</html>
```